The Orchard Desk Method: Lift Margins, Rally Teams and Mend the Commons

The book is targeting business leaders and managers. I would like to see designs that include one or more of the following: the planet, environment, healthy whole plant-based food, workplaces, offices, business profits, employee engagement. Font text for cover should be clean lines and conservative. 6" x 9" book that will be self published through Brindlewick. This should also include the book spine and back cover (text for back cover attached). The author is Hester Vaughan. ISBN will be provided.

Business

```html
<!DOCTYPE html>
<html lang="en">
<head>
<meta charset="utf-8">
<title>The Orchard Desk Method — Book Wrap</title>
<link rel="stylesheet" href="https://fonts.googleapis.com/css2?family=Cinzel:wght@400;500&family=Crimson+Text&display=swap">
<style>
  :root {
    --forest: #163813;
    --paper: #ffffff;
    --backdrop: #f1f1f1;
    --ink: #1c1c1c;
    --ember: #e5391f;
    --ember-deep: #c92a16;
    --ember-soft: #f3a08f;
    --lagoon: #2de3ea;
    --lagoon-soft: #9ef1f3;
  }
  * { box-sizing: border-box; margin: 0; padding: 0; }
  html, body { width: 899px; height: 1200px; overflow: hidden; background: var(--backdrop); }

  .wrap {
    position: absolute; left: 0; top: 289px;
    width: 899px; height: 622px;
    background: var(--forest);
  }
  .panel { position: absolute; background: var(--paper); top: 201px; height: 308px; }
  .panel--back { left: 0; width: 415px; }
  .panel--front { left: 485px; width: 414px; }

  /* Back cover */
  .emblem {
    position: absolute; left: 117px; top: 70px; width: 171px; height: 82px;
    border-radius: 50%;
    background: radial-gradient(ellipse at 50% 50%,
      var(--lagoon) 0%, var(--lagoon) 22%, var(--lagoon-soft) 32%,
      var(--ember-soft) 44%, var(--ember) 60%, rgba(201, 42, 22, 0) 72%);
  }
  .blurb {
    position: absolute; left: 42px; top: 234px; width: 337px;
    font-family: "Crimson Text", Georgia, serif;
    font-size: 11.4px; line-height: 13.4px; color: var(--ink);
    text-align: justify;
  }
  .barcode-box {
    position: absolute; left: 34px; top: 533px; width: 93px; height: 57px;
    background: var(--paper);
  }

  /* Spine */
  .spine {
    position: absolute; left: 415px; top: 0; width: 70px; height: 622px;
    color: var(--paper); font-family: "Crimson Text", Georgia, serif;
  }
  .spine__title, .spine__author {
    position: absolute; left: 50%; transform: translateX(-50%);
    writing-mode: vertical-rl; font-size: 16px; letter-spacing: 0.5px;
    text-transform: uppercase; white-space: nowrap;
  }
  .spine__title { top: 34px; }
  .spine__author { top: 420px; }

  /* Front cover */
  .front-title {
    position: absolute; left: 485px; top: 30px; width: 414px;
    text-align: center; color: var(--paper);
    font-family: "Cinzel", "Times New Roman", serif; font-weight: 400;
    line-height: 1;
  }
  .front-title span { display: block; }
  .front-title .t1 { font-size: 50px; }
  .front-title .t2 { font-size: 44px; margin-top: 2px; }
  .front-title .t3 { font-size: 58px; margin-top: 2px; text-transform: uppercase; }

  .subtitle {
    position: absolute; left: 485px; top: 236px; width: 414px;
    text-align: center; color: var(--ink);
    font-family: "Cinzel", "Times New Roman", serif;
    font-size: 14px; letter-spacing: 4.6px; line-height: 18px;
  }
  .cover-art {
    position: absolute; left: 504px; top: 292px; width: 395px; height: 152px;
    background:
      radial-gradient(ellipse 32% 52% at 50% 52%,
        var(--lagoon) 0%, var(--lagoon) 55%, var(--lagoon-soft) 78%, rgba(255,255,255,0) 100%),
      radial-gradient(ellipse 62% 62% at 50% 50%,
        var(--ember) 0%, var(--ember) 45%, var(--ember-deep) 70%, rgba(229, 57, 31, 0) 100%);
  }
  .author {
    position: absolute; left: 485px; top: 543px; width: 414px;
    text-align: center; color: var(--paper);
    font-family: "Cinzel", "Times New Roman", serif;
    font-size: 34px; letter-spacing: 2px; text-transform: uppercase;
  }
</style>
</head>
<body>
  <main class="wrap">
    <section class="back-cover">
      <div class="emblem" role="img" aria-label="Emblem: a turquoise globe circled by two red arrows"></div>
      <div class="panel panel--back"></div>
      <p class="blurb">The Orchard Desk Method provides a unique perspective targeting the corporate community to consider the business case for changing the food environment. This book is comprised of three main sections:<br>
      (1) What the medical literature says about links among lifestyle, environment, and chronic diseases, as well as what prevents (or reverses) these diseases. This section also explores scientific literature on the best food system sustainability practices for a growing population.<br>
      (2) The business case for implementing the Orchard Desk method, from both a financial perspective and from the vantage point of philosophical rationale. Namely, what poor employee health costs employers in terms of medical expenses and the reduced productivity associated with absenteeism and presenteeism, paired with the ethical rationale for an Orchard Desk workplace as a socially responsible practice that builds strong social capital with employees, customers and other stakeholders.<br>
      (3) A change model and practical strategies an organization can apply that engage employees in implementing the Orchard Desk method.<br>
      This book wraps up by challenging the reader to make it personal.</p>
      <div class="barcode-box"></div>
    </section>

    <section class="spine">
      <span class="spine__title">The Orchard Desk Method</span>
      <span class="spine__author">Hester Vaughan</span>
    </section>

    <section class="front-cover">
      <div class="panel panel--front"></div>
      <h1 class="front-title">
        <span class="t1">The</span>
        <span class="t2">Orchard Desk</span>
        <span class="t3">Method</span>
      </h1>
      <p class="subtitle">LIFT MARGINS, RALLY TEAMS<br>AND MEND THE COMMONS</p>
      <div class="cover-art" role="img" aria-label="Illustration: two office workers in silhouette reaching toward a turquoise globe of the planet, encircled by two red recycling arrows"></div>
      <p class="author">Hester Vaughan</p>
    </section>
  </main>
</body>
</html>
```